Single Page Production Company Site

Clean. Simple. Minimalist site with one page.

No portfolio, just some text to communicate a general overview of what the company does.

We work for a very select group of clients, creating strong brand personalities online. The site is specifically minimal and not communicating too much about what we do.. we have a variety of capabilities to work with clients and prefer to be broad with just a simple landing page as the point of contact for our brand.
Updates

Christmas holidays are coming up, maybe people need some time away from work with family and friends... We can keep working on this and I will provide feedback as quickly as possible, but I understand if designers have other commitments during the coming days. Thanks for your hard work!

Industry/Entity Type

Design Agency

Coding

Coded - Design and coding required

Number of Pages Required

1 page

Font styles to use
Sans Serif

Requirements
Must have
• Clean, bold text headlines.
Nice to have
• Unsure about any images used in the design, would like to see options with or without.

```html
<!DOCTYPE html>
<html lang="en">
<head>
<meta charset="utf-8">
<title>Harborline Development</title>
<link href="https://fonts.googleapis.com/css2?family=Open+Sans:wght@400;600;700&display=swap" rel="stylesheet">
<style>
:root{
  --crimson:#c8174a;
  --ink:#222;
  --text:#555;
  --stage:#e6e6e6;
  --blush:#fbeef2;
  --lilac:#eceefe;
  --field:#dcdde6;
  --violet:#5b63ee;
}
*{margin:0;padding:0;box-sizing:border-box}
html,body{width:1200px;height:1200px;overflow:hidden;background:var(--stage);font-family:"Open Sans",sans-serif}
.page{position:absolute;left:368.8px;top:0;width:580px;height:1500px;background:#fff;transform:scale(.8);transform-origin:0 0;overflow:hidden}
.abs{position:absolute}
.topbar{left:0;top:0;width:580px;height:30px;background:var(--crimson)}
.brand{left:72px;top:9px;color:#fff;font-size:8px;font-weight:600}
.nav{top:11px;color:#fff;font-size:6px}
.search{left:420px;top:8px;width:87px;height:14px;border:1px solid #fff;color:#fff;font-size:5px;padding:3px 4px}
.hero-bg{left:0;top:30px;width:580px;height:320px;background:
  radial-gradient(ellipse 160px 200px at 40px 130px,#fde8ef 0,transparent 70%),
  radial-gradient(ellipse 200px 220px at 540px 120px,#e9e9fd 0,transparent 70%),
  linear-gradient(#fbf6fb,#fff)}
h1.hero-title{left:72px;top:240px;font-size:14px;color:var(--crimson);font-weight:700}
.hero-copy{left:72px;top:265px;width:220px;font-size:6px;color:var(--text);line-height:1.4}
.btn{background:var(--crimson);color:#fff;font-size:5.5px;display:flex;align-items:center;justify-content:center}
.field{background:#fff;border:1px solid var(--field);font-size:5px;color:var(--text);padding:3px 4px}
.field.pink{border-color:#f1b5c6;border-radius:4px;font-size:5.5px;padding:4px 5px}
.feature{text-align:center;width:118px}
.feature h3{font-size:7.5px;font-weight:600;color:var(--ink);margin-bottom:4px}
.feature p{font-size:4.6px;color:var(--text);line-height:1.55}
.feature a{display:block;font-size:5px;color:var(--crimson);margin-top:3px}
.feature-card{left:227px;top:342px;width:125px;height:113px;background:var(--blush)}
.feature-icon{width:34px;height:34px;border-radius:8px}
.sec-title{font-size:10px;font-weight:700;color:var(--crimson)}
.sec-copy{font-size:5.2px;color:var(--text);line-height:1.65}
.center{text-align:center}
.foot-link{top:1431px;font-size:5.5px;color:var(--ink)}
.footbar{left:0;top:1469px;width:580px;height:31px;background:var(--crimson)}
</style>
</head>
<body>
<div class="page">
  <div class="abs hero-bg"></div>
  <header>
    <div class="abs topbar"></div>
    <div class="abs brand">Harborlinedevelopment</div>
    <nav>
      <span class="abs nav" style="left:230px">Home</span>
      <span class="abs nav" style="left:263px">About</span>
      <span class="abs nav" style="left:296px">Portfolio</span>
      <span class="abs nav" style="left:335px">Services</span>
      <span class="abs nav" style="left:373px">Contact</span>
    </nav>
    <div class="abs search">Search...</div>
    <svg class="abs" style="left:498px;top:11px" width="8" height="8" viewBox="0 0 8 8"><circle cx="3.3" cy="3.3" r="2.3" fill="none" stroke="#fff"/><line x1="5" y1="5" x2="7.5" y2="7.5" stroke="#fff"/></svg>
  </header>

  <section class="hero">
    <div class="abs" role="img" aria-label="Illustration of two people working with web screens on a blue shape" style="left:100px;top:40px;width:162px;height:182px;background:radial-gradient(circle at 55% 50%,var(--violet),#7b83f5 70%,#c6c9fb);border-radius:45% 55% 48% 52%"></div>
    <h1 class="abs hero-title">Concept. create. complete</h1>
    <p class="abs hero-copy">We are leading the way in design innovation for modern websites. Clean, functional,intuitive websites for progressive businesses.</p>
    <div class="abs btn" style="left:72px;top:293px;width:62px;height:16px">Learn More....</div>

    <div class="abs btn" style="left:390px;top:91px;width:117px;height:24px;font-weight:700">CONTACT FORM</div>
    <div class="abs field" style="left:390px;top:126px;width:117px;height:15px">Name</div>
    <div class="abs field" style="left:390px;top:148px;width:117px;height:15px">Email</div>
    <div class="abs field" style="left:390px;top:171px;width:117px;height:15px">Phone</div>
    <div class="abs field" style="left:390px;top:193px;width:117px;height:35px">Massage</div>
    <div class="abs btn" style="left:390px;top:233px;width:117px;height:14px">Send Message</div>
  </section>

  <section class="features">
    <div class="abs feature-card"></div>
    <div class="abs feature-icon" role="img" aria-label="Design tool icon" style="left:135px;top:350px;background:linear-gradient(135deg,#fde3c4,#f6d0d6)"></div>
    <div class="abs feature" style="left:93px;top:396px">
      <h3>Design happens here</h3>
      <p>We are leading the way in design innovation for modern websites. Clean, functional,intuitive websites for progressive businesses.</p>
      <a>Read More...</a>
    </div>
    <div class="abs feature-icon" role="img" aria-label="Colour and art icon" style="left:273px;top:352px;background:linear-gradient(135deg,#fbd7b8,#d7e6f0)"></div>
    <div class="abs feature" style="left:231px;top:398px">
      <h3 style="color:var(--crimson);font-weight:400">Art happens here</h3>
      <p>Building brands through design, we believe that contrast is everything. For industry leaders who set the pace and exceed</p>
      <a>Read More...</a>
    </div>
    <div class="abs feature-icon" role="img" aria-label="Ideas icon" style="left:411px;top:350px;background:linear-gradient(135deg,#fcedc0,#d9edf6)"></div>
    <div class="abs feature" style="left:369px;top:396px">
      <h3>Ideas happen here</h3>
      <p>Clients look to us for unique, exceptional solutions to their technology issues. We bring creativity to the table and solve.</p>
      <a>Read More...</a>
    </div>
  </section>

  <section class="team">
    <div class="abs" role="img" aria-label="Team photo of four smiling colleagues giving thumbs up" style="left:72px;top:488px;width:158px;height:150px;background:linear-gradient(135deg,#c9c9cc,#6e6b6f 60%,#3a3840);border-radius:52% 48% 45% 55%"></div>
    <h2 class="abs sec-title" style="left:262px;top:527px">THE HARBOR TEAM</h2>
    <p class="abs sec-copy" style="left:262px;top:545px;width:222px">Harborline Development Company focuses on creating extraordinary online experiences forextraordinary clients. We'll work with you to create the perfect online presence for yourbrand.</p>
    <div class="abs btn" style="left:262px;top:581px;width:55px;height:16px">Read More...</div>
  </section>

  <section class="size">
    <div class="abs" role="img" aria-label="Isometric illustration of people building a web dashboard" style="left:72px;top:670px;width:148px;height:142px;background:radial-gradient(circle at 50% 45%,#c7cbfb,#e9eafd 70%);border-radius:48% 52% 55% 45%"></div>
    <h2 class="abs sec-title" style="left:257px;top:690px">Size is Everything.</h2>
    <p class="abs sec-copy" style="left:257px;top:711px;width:232px">We don't work in a massive corporate office and we don't have a mailroom. Not that there's anything wrong with that, it's just that we like knowing each other's names, and encourage our clients to know ours. Our small staff has an advantage – our group works more efficiently, more cost-effectively and most importantly, flexible to each client's unique needs. We deliver a range of services found at any agency, with the personal service you should expect.</p>
    <div class="abs btn" style="left:257px;top:775px;width:56px;height:16px">Read More...</div>
  </section>

  <section class="goal">
    <h2 class="abs sec-title" style="left:222px;top:870px;width:100px;text-align:right">Our Goal</h2>
    <p class="abs sec-copy" style="left:92px;top:891px;width:230px;text-align:right">Harborline Development brings your brand to life, online. We do it all when it comes to online commerce for retail stores, wholesalers and distributors. Taking your company online introduces a world of opportunity, as well as specific challenges associated with online trade. We'll assist you in establishing a successful online presence and bringing your brand to a worldwide audience</p>
    <div class="abs btn" style="left:266px;top:945px;width:55px;height:16px">Read More...</div>
    <div class="abs" role="img" aria-label="Isometric illustration of growth charts with small figures" style="left:360px;top:845px;width:147px;height:143px;background:radial-gradient(circle at 50% 50%,#b7bdf8,#e6e8fd 70%);border-radius:55% 45% 50% 50%"></div>
  </section>

  <section class="founder">
    <div class="abs" role="img" aria-label="Illustration of a connected network of people" style="left:72px;top:1020px;width:148px;height:142px;background:radial-gradient(circle at 50% 50%,#cdd0fb,#eceefe 70%);border-radius:50% 50% 46% 54%"></div>
    <h2 class="abs sec-title" style="left:257px;top:1039px">Who's Miles?</h2>
    <p class="abs sec-copy" style="left:257px;top:1060px;width:242px">Miles Porter, owner of Harborline Development is not your typical principal. He's worked internationally with both Norbridge and Kellan Press publications in photo production for titles including Metro Style and Gallery Monthly. Originally from coastal Maine and an allaround New Englander, Miles can often be found sailing during the summer and skiing during winter.He believes that inspiration comes from experiencing the world, not from sitting in a cubicle. But no worries,</p>
    <div class="abs btn" style="left:257px;top:1124px;width:56px;height:16px">Read More...</div>
  </section>

  <section class="contact">
    <h2 class="abs center" style="left:0;top:1191px;width:580px;font-size:10px;font-weight:400;color:var(--crimson)">WE GET YOU</h2>
    <p class="abs sec-copy center" style="left:125px;top:1215px;width:330px">Having a website isn't enough. You need to show your customers you understand thesocially connected onlineworld we live in.We help you create designs that capture the personality of your business and projectthe imageyou want your customers to see.Maybe you're a small company looking tosell yourselfin the big leagues;maybe you're a big company thatwants to lookapproachable;either way, we can make it happen.</p>
    <div class="abs field pink" style="left:192px;top:1264px;width:196px;height:15px">Name</div>
    <div class="abs field pink" style="left:192px;top:1287px;width:196px;height:15px">Email</div>
    <div class="abs field pink" style="left:192px;top:1310px;width:196px;height:15px">Phone</div>
    <div class="abs field pink" style="left:192px;top:1333px;width:196px;height:39px">Message</div>
    <div class="abs btn" style="left:260px;top:1382px;width:60px;height:16px;border-radius:3px;font-size:5px">SEND MESSAGE</div>
  </section>

  <footer>
    <div class="abs" style="left:-40px;top:1370px;width:140px;height:120px;border-radius:50%;background:radial-gradient(#fdeef2,transparent 70%)"></div>
    <div class="abs" style="left:420px;top:1400px;width:200px;height:100px;border-radius:50%;background:radial-gradient(#f0f1fd,transparent 70%)"></div>
    <span class="abs foot-link" style="left:72px;color:var(--crimson)">Home</span>
    <span class="abs foot-link" style="left:99px">About</span>
    <span class="abs foot-link" style="left:127px">Portfolio</span>
    <span class="abs foot-link" style="left:161px">Services</span>
    <span class="abs foot-link" style="left:194px">Contact</span>
    <svg class="abs" style="left:328px;top:1431px" width="11" height="8" viewBox="0 0 11 8"><rect x=".5" y=".5" width="10" height="7" fill="none" stroke="var(--crimson)"/><path d="M.5 .5l5 4 5-4" fill="none" stroke="var(--crimson)"/></svg>
    <span class="abs foot-link" style="left:343px;font-size:6px">hello@harborlinedev.com</span>
    <svg class="abs" style="left:443px;top:1430px" width="9" height="9" viewBox="0 0 9 9"><path d="M1.5 1l2 0 1 2-1.2 1a5 5 0 0 0 2 2l1-1.2 2 1v2c-4 0-6.8-2.8-6.8-6.8z" fill="none" stroke="var(--crimson)" stroke-width=".8"/></svg>
    <span class="abs foot-link" style="left:457px;font-size:6px">+1-404-555-0172</span>
    <div class="abs footbar"></div>
    <span class="abs" style="left:72px;top:1481px;font-size:5px;color:#fff">@harborlinedevelopment 2018</span>
    <svg class="abs" style="left:446px;top:1477px" width="62" height="14" viewBox="0 0 62 14" aria-label="Social links">
      <circle cx="7" cy="7" r="5.5" fill="none" stroke="#fff" stroke-width=".8"/>
      <circle cx="23" cy="7" r="5.5" fill="none" stroke="#fff" stroke-width=".8"/>
      <circle cx="39" cy="7" r="5.5" fill="none" stroke="#fff" stroke-width=".8"/>
      <circle cx="55" cy="7" r="5.5" fill="none" stroke="#fff" stroke-width=".8"/>
    </svg>
  </footer>
</div>
</body>
</html>
```